Velvet Lantern rebranding my business with a new business card

I have my new logo and now I need a refresher on my business cards. I really want something fun and fresh. I like black background or anything to make the color pop.
Logo
Name: Velvet Lantern
Contact Info as stated below:
Mara Pelkin
519-555-0147
Logo
Name: Velvet Lantern
Mara Pelkin
519-555-0147
fb.me/VelvetLanternbyMara
Instagram: @VelvetLanternbyMara

Industry/Entity Type

Business

Contact Information for Business Card

double-sided. Logo on one side. Contact info on the other.

Requirements
Must have
• Logo
• Name: Velvet Lantern
• Contact Info as stated below:
• Mara Pelkin
• 519-555-0147
• fb.me/VelvetLanternbyMara
• fb.me/VelvetLanternbyMara

```html
<!DOCTYPE html>
<html lang="en">
<head>
<meta charset="utf-8">
<title>Velvet Lantern – Business Card</title>
<link href="https://fonts.googleapis.com/css2?family=Roboto:wght@400;500;700&display=swap" rel="stylesheet">
<style>
  :root {
    --stage: #ece8e3;
    --card-white: #ffffff;
    --card-black: #1b1b1d;
    --blush: #f2b8c6;
    --ink: #2b2b2b;
    --muted: #6f6f6f;
    --text-light: #ffffff;
  }
  html, body {
    margin: 0;
    padding: 0;
    width: 1200px;
    height: 960px;
    overflow: hidden;
    background: var(--stage);
    font-family: "Roboto", Arial, sans-serif;
  }
  .canvas {
    position: relative;
    width: 1200px;
    height: 960px;
  }
  .card {
    position: absolute;
    border-radius: 16px;
    overflow: hidden;
    box-shadow: 0 4px 10px rgba(0,0,0,0.18);
  }

  /* Logo side */
  .card--logo {
    left: 320px; top: 95px;
    width: 605px; height: 360px;
    background: var(--card-white);
  }
  .logo-ring {
    position: absolute;
    left: 199px; top: 74px;
    width: 200px; height: 200px;
    border-radius: 50%;
    border: 2px solid var(--blush);
    box-shadow: 0 0 0 4px var(--card-white), 0 0 0 5px var(--ink);
    display: flex;
    align-items: center;
    justify-content: center;
  }
  .logo-name {
    font-weight: 700;
    color: var(--ink);
    text-align: center;
    line-height: 1.1;
  }
  .logo-ring .logo-name { font-size: 22px; }
  .card-web {
    position: absolute;
    left: 0; right: 0; top: 316px;
    text-align: center;
    font-size: 15px;
    letter-spacing: 0.33em;
    color: var(--muted);
  }

  /* Contact side */
  .card--contact {
    left: 320px; top: 492px;
    width: 600px; height: 342px;
    background: var(--card-black);
  }
  .card-shape {
    position: absolute;
    inset: 0;
  }
  .card--contact .logo-name {
    position: absolute;
    left: 20px; top: 140px;
    width: 290px;
    font-size: 38px;
  }
  .holder-name {
    position: absolute;
    right: 30px; top: 34px;
    margin: 0;
    font-size: 20px;
    font-weight: 700;
    color: var(--text-light);
    letter-spacing: 0.01em;
  }
  .contact-list {
    position: absolute;
    right: 30px; top: 253px;
    margin: 0; padding: 0;
    list-style: none;
    color: var(--text-light);
    font-size: 15px;
  }
  .contact-list li {
    display: flex;
    align-items: center;
    justify-content: flex-end;
    gap: 8px;
    height: 20px;
  }
  .contact-icon {
    width: 13px; height: 13px;
    flex: none;
  }
</style>
</head>
<body>
<div class="canvas">

  <section class="card card--logo">
    <div class="logo-ring">
      <span class="logo-name">Velvet<br>Lantern</span>
    </div>
    <p class="card-web">www.velvetlantern.com</p>
  </section>

  <section class="card card--contact">
    <svg class="card-shape" width="600" height="342" viewBox="0 0 600 342">
      <circle cx="162" cy="171" r="226" fill="var(--card-white)"/>
      <circle cx="162" cy="171" r="219" fill="none" stroke="var(--blush)" stroke-width="2"/>
      <circle cx="162" cy="171" r="213" fill="none" stroke="var(--blush)" stroke-width="1.5"/>
    </svg>

    <span class="logo-name">Velvet Lantern</span>

    <h1 class="holder-name">MARA PELKIN</h1>

    <ul class="contact-list">
      <li>519-555-0147
        <svg class="contact-icon" viewBox="0 0 24 24"><path fill="#fff" d="M6.6 10.8a15.1 15.1 0 0 0 6.6 6.6l2.2-2.2c.3-.3.7-.4 1-.2 1.1.4 2.3.6 3.6.6.6 0 1 .4 1 1V20c0 .6-.4 1-1 1C10.6 21 3 13.4 3 4c0-.6.4-1 1-1h3.5c.6 0 1 .4 1 1 0 1.2.2 2.4.6 3.6.1.3 0 .7-.2 1z"/></svg>
      </li>
      <li>www.velvetlantern.com
        <svg class="contact-icon" viewBox="0 0 24 24"><circle cx="12" cy="12" r="10" fill="none" stroke="#fff" stroke-width="2"/><path d="M2 12h20M12 2c3 3 3 17 0 20M12 2c-3 3-3 17 0 20" fill="none" stroke="#fff" stroke-width="1.6"/></svg>
      </li>
      <li>fb.me/VelvetLanternbyMara
        <svg class="contact-icon" viewBox="0 0 24 24"><rect x="2" y="2" width="20" height="20" rx="2" fill="#fff"/></svg>
      </li>
    </ul>
  </section>

</div>
</body>
</html>
```